All-Natural Head Lice Removal company

I need a business card with my pre-existing logo. We are a new company located in Portland Oregon that goes into peoples homes to help with head lice removal. My products and approach are all- natural and also will be around children.On my current logo we used Teal Bl and the color Green. I am open to new ideas just want it simple and creative

Target Market(s)

my biggest market is families of school aged children

Industry/Entity Type

Business

Contact Information for Business Card

see upload for details from previous business card

Font styles to use
Serif

Colors
33a6d7
9bcb3b
f37122

Requirements
Must have
• Basic information/ logo put into a creative format that is catching to the eye
Nice to have
• creative

```html
<!DOCTYPE html>
<html lang="en">
<head>
<meta charset="utf-8">
<title>NitPick Home – Business Card</title>
<link rel="stylesheet" href="https://fonts.googleapis.com/css2?family=Arvo:wght@400;700&family=Open+Sans:wght@400;600&display=swap">
<style>
  :root {
    --teal: #33a6d7;
    --teal-light: #7ccdee;
    --green: #9bcb3b;
    --ink: #2b2b2b;
    --charcoal: #3a3a3a;
    --paper: #ffffff;
    --stage: #ecebe8;
  }
  * { box-sizing: border-box; margin: 0; padding: 0; }
  html, body { width: 1200px; height: 913px; overflow: hidden; }
  body {
    background: var(--stage);
    font-family: "Arvo", Georgia, serif;
    color: var(--ink);
    position: relative;
  }
  .card {
    position: absolute;
    width: 520px;
    height: 297px;
    background: var(--paper);
    box-shadow: 0 4px 14px rgba(0,0,0,.12);
    overflow: hidden;
  }
  .card--front { left: 60px; top: 150px; }
  .card--back { left: 620px; top: 466px; }

  /* front */
  .front-tagline {
    position: absolute; left: 100px; top: 46px;
    font-size: 15px; letter-spacing: .2px; white-space: nowrap;
  }
  .contact-band {
    position: absolute; left: 0; top: 96px;
    width: 476px; height: 68px;
    background: linear-gradient(90deg, var(--teal) 0%, var(--teal-light) 100%);
  }
  .edge-blocks { position: absolute; right: 0; top: 84px; }
  .stripe-blocks { position: absolute; left: 0; top: 150px; }
  .contact-list {
    position: absolute; right: 64px; top: 104px;
    list-style: none; text-align: right;
    font-size: 12px; line-height: 17px; color: var(--ink);
    white-space: nowrap;
  }
  .contact-icons { position: absolute; right: 46px; top: 106px; }

  .brand-name {
    position: absolute;
    font-family: "Arvo", Georgia, serif;
    font-weight: 700;
    color: var(--charcoal);
    white-space: nowrap;
  }
  .brand-name--front { left: 60px; top: 200px; font-size: 28px; line-height: 34px; }
  .brand-name--back { left: 0; right: 0; top: 88px; text-align: center; font-size: 36px; line-height: 42px; }

  .holder {
    position: absolute; right: 44px; top: 182px; text-align: right;
  }
  .holder__name { font-size: 20px; letter-spacing: .5px; white-space: nowrap; }
  .holder__role {
    font-family: "Open Sans", Arial, sans-serif;
    font-size: 11px; color: var(--teal); letter-spacing: .5px; margin-top: 2px;
  }

  /* back */
  .back-copy {
    position: absolute; left: 0; right: 0; top: 186px;
    text-align: center; font-size: 13px; line-height: 17px;
  }
  .back-copy .slogan { font-weight: 700; }
  .back-copy .web { color: var(--teal); }
</style>
</head>
<body>

<section class="card card--front" aria-label="Business card front">
  <p class="front-tagline">All Natural In-Home Lice Removal Services</p>

  <div class="contact-band"></div>

  <svg class="edge-blocks" width="44" height="24" viewBox="0 0 44 24" aria-hidden="true">
    <rect x="0" y="0" width="14" height="12" fill="#3a3a3a"/>
    <rect x="14" y="0" width="30" height="12" fill="#9bcb3b"/>
    <rect x="0" y="12" width="30" height="12" fill="#9bcb3b"/>
    <rect x="30" y="12" width="14" height="12" fill="#3a3a3a"/>
  </svg>

  <svg class="stripe-blocks" width="48" height="42" viewBox="0 0 48 42" aria-hidden="true">
    <rect x="0" y="0" width="16" height="14" fill="#9bcb3b"/>
    <rect x="16" y="0" width="16" height="14" fill="#3a3a3a"/>
    <rect x="32" y="0" width="16" height="14" fill="#9bcb3b"/>
    <rect x="0" y="14" width="16" height="14" fill="#3a3a3a"/>
    <rect x="16" y="14" width="16" height="14" fill="#9bcb3b"/>
    <rect x="0" y="28" width="16" height="14" fill="#9bcb3b"/>
  </svg>

  <ul class="contact-list">
    <li>1-800-555-0142</li>
    <li>dana@nitpickhome.com</li>
    <li>www.nitpickhome.com</li>
  </ul>

  <svg class="contact-icons" width="12" height="50" viewBox="0 0 12 50" aria-hidden="true">
    <path d="M2 1 L5 1 L6 4 L4.5 5.5 Q6 8 8 9.5 L9.5 8 L12 9 L12 12 Q5 12 1 4 Z" fill="#fff"/>
    <rect x="0.5" y="19" width="11" height="8" fill="none" stroke="#fff" stroke-width="1.2"/>
    <path d="M0.5 19 L6 24 L11.5 19" fill="none" stroke="#fff" stroke-width="1.2"/>
    <circle cx="6" cy="40" r="5.2" fill="none" stroke="#fff" stroke-width="1.2"/>
    <path d="M1 40 H11 M6 35 V45" stroke="#fff" stroke-width="1"/>
  </svg>

  <p class="brand-name brand-name--front">NitPick Home</p>

  <div class="holder">
    <p class="holder__name">DANA MERROW</p>
    <p class="holder__role">OWNER</p>
  </div>
</section>

<section class="card card--back" aria-label="Business card back">
  <p class="brand-name brand-name--back">NitPick Home</p>
  <div class="back-copy">
    <p class="slogan">Try NitPick Home Today and Be Lice Free Tomorrow!</p>
    <p>All Natural In-Home Lice Removal Services</p>
    <p class="web">www.nitpickhome.com</p>
  </div>
</section>

</body>
</html>
```